Premium Honey Fusions need a label design. 5 awesome blends (see below)

We need a label design for a line of honey. Brand is an existing brand called MELVORIK. www.melvorikusa.example
MELVORIK is a line of juices. The honey line is an extension of the MELVORIK juice line.
Blends are:
Honey Cinnamon
Honey Saffron
Honey Ginger
Honey Herbs
Honey Wild Flower
PRODUCT FROM INDIA
We need a label design for a line of honey. Brand is an existing brand called MELVORIK.
See www.melvorikusa.example
We would like to see label designs that:
-are easy to read, clean
-"Honey Cinnamon”, etc... should be prominent, as it will be what will set us apart.
-use colors that communicate "premium honey"
-premium
-unique
-healthy/good for you
-We need a “Help us save the bees” type message on the logo. We will give % of profit from sale of honey to go towards saving the bees.
The final design should communicate :
-healthy
-DELICIOUS!!!! (it is!)
-premium
-unique
-exotic
Glass bottle is square (see pics) and label has 3 sides:
Front panel
Side panel 1: will be nutritional, ingredients, UPC, etc
Side panel 2: a story about bees? about saffron, about cinnamon??
Target Market(s)
Hispanic and American markets.
Healthy conscious people.
Premium honey market
Look and feel

```html
<!DOCTYPE html>
<html lang="en">
<head>
<meta charset="utf-8">
<title>MELVORIK Honey Labels</title>
<link href="https://fonts.googleapis.com/css2?family=Lobster&family=Josefin+Sans:wght@400;700&display=swap" rel="stylesheet">
<style>
  :root {
    --backdrop: #ececec;
    --frame-brown: #3d2010;
    --rim-white: #ffffff;
    --honey-yellow: #f8d53a;
    --text-white: #ffffff;
    --herbs-glow: #8ba63a;
    --flower-glow: #7a3f8c;
    --seal-red: #c41e2e;
    --seal-dark: #7e0f1a;
    --brand-red: #d8242f;
  }
  html, body {
    margin: 0;
    width: 1200px;
    height: 1000px;
    overflow: hidden;
    background: radial-gradient(ellipse at center, #f7f7f7 0%, var(--backdrop) 75%);
  }
  .canvas { position: relative; width: 1200px; height: 1000px; }
  .label {
    position: absolute;
    top: 130px;
    width: 369px;
    height: 700px;
  }
  .label--herbs { left: 163px; }
  .label--wildflower { left: 653px; }
  .label__shape { position: absolute; inset: 0; }
  .label__title {
    position: absolute;
    left: 0; right: 0;
    top: 255px;
    text-align: center;
    font-family: "Lobster", cursive;
    font-size: 122px;
    line-height: 1;
    color: var(--honey-yellow);
    text-shadow: 4px 6px 8px rgba(0,0,0,0.45);
  }
  .label__blend {
    position: absolute;
    left: 0; right: 0;
    top: 388px;
    text-align: center;
    font-family: "Lobster", cursive;
    font-size: 40px;
    line-height: 1;
    color: var(--text-white);
    text-shadow: 2px 3px 5px rgba(0,0,0,0.45);
    transform: rotate(-3deg);
  }
  .label__weight {
    position: absolute;
    left: 21px;
    top: 658px;
    font-family: "Josefin Sans", sans-serif;
    font-size: 19px;
    color: var(--text-white);
  }
  .label__brand {
    position: absolute;
    right: 22px;
    top: 650px;
    font-family: "Josefin Sans", sans-serif;
    font-weight: 700;
    font-size: 19px;
    color: var(--brand-red);
    background: var(--honey-yellow);
    padding: 7px 8px 4px;
    border-radius: 4px;
  }
</style>
</head>
<body>
<main class="canvas">

  <section class="label label--herbs">
    <svg class="label__shape" width="369" height="700" viewBox="0 0 369 700">
      <defs>
        <radialGradient id="herbsGlow" cx="50%" cy="55%" r="55%">
          <stop offset="0%" stop-color="var(--herbs-glow)"/>
          <stop offset="100%" stop-color="#3f2412"/>
        </radialGradient>
        <radialGradient id="sealWax" cx="45%" cy="40%" r="60%">
          <stop offset="0%" stop-color="#e03040"/>
          <stop offset="100%" stop-color="var(--seal-dark)"/>
        </radialGradient>
        <radialGradient id="jarTone" cx="50%" cy="50%" r="50%">
          <stop offset="0%" stop-color="#4a2a14" stop-opacity="0.75"/>
          <stop offset="100%" stop-color="#4a2a14" stop-opacity="0"/>
        </radialGradient>
      </defs>
      <path d="M0,698 V326.5 A184.5,184.5 0 0 1 369,326.5 V698 Z" fill="var(--frame-brown)"/>
      <path d="M9,689 V326.5 A175.5,175.5 0 0 1 360,326.5 V689 Z" fill="url(#herbsGlow)" stroke="var(--rim-white)" stroke-width="2"/>
      <ellipse cx="184" cy="540" rx="95" ry="110" fill="url(#jarTone)" role="img" aria-label="Engraved illustration of a honey jar with dipper and honeycomb on a plate"/>
      <g class="seal" role="img" aria-label="Red wax seal with ribbon and bee emblem">
        <circle cx="184.5" cy="115" r="80" fill="url(#sealWax)"/>
        <circle cx="184.5" cy="115" r="56" fill="none" stroke="var(--seal-dark)" stroke-width="2"/>
        <text x="184.5" y="85" text-anchor="middle" font-family="Josefin Sans, sans-serif" font-weight="700" font-size="13" fill="var(--seal-dark)">HELP US</text>
        <text x="184.5" y="155" text-anchor="middle" font-family="Josefin Sans, sans-serif" font-weight="700" font-size="12" fill="var(--seal-dark)">SAVE THE BEES</text>
      </g>
    </svg>
    <div class="label__title">Honey</div>
    <div class="label__blend">Herbs</div>
    <div class="label__weight">8oz. (226g)</div>
    <div class="label__brand">MELVORIK</div>
  </section>

  <section class="label label--wildflower">
    <svg class="label__shape" width="369" height="700" viewBox="0 0 369 700">
      <defs>
        <radialGradient id="flowerGlow" cx="50%" cy="55%" r="55%">
          <stop offset="0%" stop-color="var(--flower-glow)"/>
          <stop offset="100%" stop-color="#3f2214"/>
        </radialGradient>
        <radialGradient id="sealWax2" cx="45%" cy="40%" r="60%">
          <stop offset="0%" stop-color="#e03040"/>
          <stop offset="100%" stop-color="var(--seal-dark)"/>
        </radialGradient>
        <radialGradient id="jarTone2" cx="50%" cy="50%" r="50%">
          <stop offset="0%" stop-color="#3e2218" stop-opacity="0.75"/>
          <stop offset="100%" stop-color="#3e2218" stop-opacity="0"/>
        </radialGradient>
      </defs>
      <path d="M0,698 V326.5 A184.5,184.5 0 0 1 369,326.5 V698 Z" fill="var(--frame-brown)"/>
      <path d="M9,689 V326.5 A175.5,175.5 0 0 1 360,326.5 V689 Z" fill="url(#flowerGlow)" stroke="var(--rim-white)" stroke-width="2"/>
      <ellipse cx="184" cy="540" rx="95" ry="110" fill="url(#jarTone2)" role="img" aria-label="Engraved illustration of a honey jar with dipper and honeycomb on a plate"/>
      <g class="seal" role="img" aria-label="Red wax seal with ribbon and bee emblem">
        <circle cx="184.5" cy="115" r="80" fill="url(#sealWax2)"/>
        <circle cx="184.5" cy="115" r="56" fill="none" stroke="var(--seal-dark)" stroke-width="2"/>
        <text x="184.5" y="85" text-anchor="middle" font-family="Josefin Sans, sans-serif" font-weight="700" font-size="13" fill="var(--seal-dark)">HELP US</text>
        <text x="184.5" y="155" text-anchor="middle" font-family="Josefin Sans, sans-serif" font-weight="700" font-size="12" fill="var(--seal-dark)">SAVE THE BEES</text>
      </g>
    </svg>
    <div class="label__title">Honey</div>
    <div class="label__blend">Wild Flower</div>
    <div class="label__weight">8oz. (226g)</div>
    <div class="label__brand">MELVORIK</div>
  </section>

</main>
</body>
</html>
```